Personal coach needs design for inspirational essay 4-page brochure

Overview:
This is a brochure, 11”x17” that folds to 8-1/2”x11” with 4 pages. Think of it as an oversize greeting card. It may be easiest to understand if you print out the copy and follow it along with descriptions below.
• Front cover: photograph of my embroidery sampler (jpeg photo attached)
• Inside spread: Copy with appropriate graphic elements that depict embroidery
• Back cover: contact information, brief descriptive copy, a thumbnail photo of original antique sampler (jpeg photo attached)
Copy for front cover title, inside spread and back cover is attached
Purpose of brochure:
Once a year, I produce a 4-page illustrated philosophical essay, which invites personal reflection on living a more mindful, meaningful life. I have this printed as hard copy. I have attached a few examples from previous years (Every Morning Brings Rain (Sketch Harbor created this for me last year), Lanterns, Letters from Willows). Each has a unique design related to its theme.
Concept:
This year’s essay theme, “I am a child of light. I walk in love and live in beauty” is based on a quote that I included in an embroidery sample that I made, which is a replica of an antique sampler. All this ls described in the copy I wrote for the inside spread.
Design Guidance:
Front cover: I want to use a photo of my actual sampler. I am not sure how big you can make it, given the resolution of the photo which I took from my Zelvo. So, the cover would include this photo plus the words “I am a child of light. I walk in love and live in beauty.” Given the colors of my embroidery, I imagine a color palette of pastel pink, green or blue – to go along with the sampler. But I am also open to suggestions.
Inside Spread: Along with the copy, I envision incorporating some graphic elements that depict the art of embroidery, e.g.: scissors, a spool of thread, a threaded needle, etc. At the end of my document with copy is a page describing some potential graphic elements to explore, along with a couple examples of line drawings of those kind of objects.
Back cover: If you look at some of the other examples I’ve sent, you’ll see how this cover is typically handled. Place a reduced thumbnail version of the actual brochure cover near the line that says this is the 17th in a series. Then, there’s a jpeg photo of the actual antique sampler that should be placed next to the copy that says “About the original sampler.” If the jpeg isn't good, look at the original on this site: https://archive.fernwoodcollections.org/objects/40512/sampler-by-edith-hallows
A couple of questions have come up for my project, relevant to all designers:
1. Ultimately, I need a print-ready pdf, complete with crop marks. I need to be able to give the printer camera-ready artwork that he can digitally print from.
2. The overall mood I'm looking for in this piece: feminine, soft elegance, subtle, flowing, very soft/pastel (think very, very pale shell pink with perhaps a cream or soft gray as accent). No photography or 4-color art. And to repeat what I said in the project description: NO sewing machines, dress forms, safety pins, irons -- use only line drawings related to embroidery, e.g.: spools of thread, threaded needles, thimble, scissors.
Thank you.

```html
<!DOCTYPE html>
<html lang="en">
<head>
<meta charset="utf-8">
<title>I Am a Child of Light – Essay Brochure</title>
<link href="https://fonts.googleapis.com/css2?family=Roboto+Slab:wght@400;700;900&display=swap" rel="stylesheet">
<style>
:root{
  --backdrop:#e4e4e4;
  --paper:#d6b891;
  --paper-light:#e2c9a6;
  --paper-dark:#c6a47c;
  --ink:#1f1a15;
  --ink-brown:#4a3323;
  --stitch:#5a4433;
  --frame:#3b1a12;
  --sampler-cream:#d9d2bf;
  --sampler-green:#8a9a7a;
  --box-tint:rgba(240,222,196,.55);
  --white:#ffffff;
}
*{margin:0;padding:0;box-sizing:border-box}
html,body{width:1037px;height:1200px;overflow:hidden;background:var(--backdrop)}
body{position:relative;font-family:"Roboto Slab",Georgia,serif;color:var(--ink)}
.spread{
  position:absolute;left:100px;width:836px;height:540px;overflow:hidden;
  background:radial-gradient(ellipse at 30% 30%,var(--paper-light),var(--paper) 55%,var(--paper-dark));
  box-shadow:3px 5px 8px rgba(0,0,0,.35);
}
.spread--outside{top:35px}
.spread--inside{top:616px}
.stitch-rule{position:absolute;height:6px;border-top:2px dotted var(--stitch);border-bottom:2px dotted var(--stitch);opacity:.8}

/* back cover */
.thumb{position:absolute;border:2px solid #2a1c14}
.thumb--cover{left:38px;top:31px;width:76px;height:92px;background:linear-gradient(180deg,#b7a98c,#8b7a5c 70%,#4d5a33)}
.thumb--antique{left:36px;top:234px;width:80px;height:116px;background:linear-gradient(180deg,#e1d3b4,#cdbb94 70%,#9f8d63)}
.series-note{
  position:absolute;left:116px;top:32px;width:265px;height:92px;
  background:var(--box-tint);padding:24px 8px 6px 8px;
  color:var(--white);font-size:10.5px;line-height:13px;
}
.series-note b{font-weight:700}
.series-note .year{position:absolute;right:8px;bottom:6px;font-weight:700;font-size:9.5px}
.contact{position:absolute;font-size:9px;line-height:11.5px;color:var(--ink-brown);white-space:nowrap}
.contact--address{left:36px;top:135px}
.contact--lines{left:247px;top:158px;width:135px}
.about-heading{position:absolute;font-weight:700;font-size:12.5px;line-height:14px;color:var(--ink-brown);text-transform:uppercase}
.about-heading--original{left:124px;top:232px}
.about-heading--samplers{left:36px;top:375px}
.about-text{position:absolute;font-size:7.6px;line-height:9.4px;color:var(--ink-brown);text-align:justify}
.about-text--original{left:124px;top:266px;width:258px}
.about-text--samplers{left:36px;top:411px;width:346px}

/* front cover */
.cover{
  position:absolute;left:427px;top:0;width:409px;height:540px;
  background:var(--frame);padding:8px;
}
.cover-photo{
  width:100%;height:100%;
  background:linear-gradient(180deg,var(--sampler-cream) 0%,#d3cab3 60%,#bfb697 78%,var(--sampler-green) 90%,#3d4a2a 100%);
}
.cover-title{
  position:absolute;right:58px;top:370px;text-align:right;color:var(--white);
  font-weight:700;text-shadow:0 1px 3px rgba(0,0,0,.35);
}
.cover-title .line{display:block;font-size:22px;line-height:29px}
.cover-title .light{display:block;font-size:55px;line-height:46px;font-weight:900;letter-spacing:1px}
.cover-tagline{
  position:absolute;left:427px;width:409px;top:479px;text-align:center;white-space:nowrap;
  color:var(--white);font-size:12.5px;font-weight:700;text-shadow:0 1px 3px rgba(0,0,0,.5)
}

/* inside spread */
.illustration{position:absolute;left:241px;top:123px;width:333px;height:298px;
  background:radial-gradient(ellipse at 50% 50%,rgba(110,80,55,.55),rgba(110,80,55,.15) 65%,transparent 72%)}
.essay-col{position:absolute;top:41px;font-size:9.4px;line-height:11.4px;color:var(--ink)}
.essay-col p{margin-bottom:11.4px}
.essay-col--left{left:40px;width:362px}
.essay-col--right{left:440px;width:358px}
.wrap-gap{float:right;width:0;height:125px}
.wrap-shape{float:right;clear:right;width:158px;height:255px}
.wrap-gap-r{float:left;width:0;height:86px}
.wrap-r1{float:left;clear:left;width:50px;height:23px}
.wrap-r2{float:left;clear:left;width:132px;height:160px}
.wrap-r3{float:left;clear:left;width:115px;height:46px}
.closing-title{
  position:absolute;left:518px;top:429px;width:281px;height:60px;
  background:rgba(240,226,205,.7);border-top:2px dotted var(--stitch);border-bottom:2px dotted var(--stitch);
  padding:4px 8px;color:var(--white);white-space:nowrap;
}
.closing-title .title{display:block;font-size:19px;line-height:22px;text-shadow:0 0 2px var(--ink-brown),0 0 1px var(--ink-brown)}
.closing-title .sub{display:block;font-size:15px;line-height:19px;color:var(--ink)}
</style>
</head>
<body>

<section class="spread spread--outside">
  <div class="thumb thumb--cover" role="img" aria-label="Reduced thumbnail of the front cover with the embroidered sampler"></div>
  <div class="series-note"><b>I am a child of light</b> is the 17th in a series of Labor Day essays inviting a moment of reflection on living a more meaningful, more mindful life<span class="year">©2024</span></div>

  <div class="contact contact--address">Mara Whitcombe Ellery, Ph.D.<br>Fieldstone House<br>18 Orchard Lane<br>Ashby Falls, Vermont&nbsp;&nbsp;05099</div>
  <div class="contact contact--lines">Mobile:&nbsp; 555-013-4478<br>Email: mwellery@lanternmail.net</div>

  <div class="stitch-rule" style="left:38px;top:195px;width:343px"></div>

  <div class="thumb thumb--antique" role="img" aria-label="Photo of the antique Chase Sampler"></div>
  <h2 class="about-heading about-heading--original">About the<br>original sampler</h2>
  <p class="about-text about-text--original">The embroidery sampler that I reproduced is a part of the Fernwood Collections textile collection and is known as “The Chase Sampler” because of the dog chasing a leaping stag. It is considered a rare example of American needlework design because it combines an embroidered picture with alphabet lists and includes the embroiderer’s name (Edith Hallows), place of birth, date the sampler was made, as well as a pious statement: Goodness and Mercy Ever follow those who shape their Conduct by Gods Holy Laws.</p>

  <h2 class="about-heading about-heading--samplers">About embroidered<br>samplers</h2>
  <p class="about-text about-text--samplers">In Colonial days, needlework skills were important for the future management of a girl’s household. Alphabets allowed girls to practice the marking of linen; sheets, undergarments and other personal items were initialed or named so they came back to their right owners after wash day. Various motifs and border patterns were used to decorate both clothes and domestic furnishings. In these times there were no pattern books, so when women saw a stitch they wanted to use, they quickly sewed a small example on a piece of cloth – their “sampler.” The completed work was usually framed and hung in the parlor as a testament to the maker’s obedience, patience, and skill.</p>

  <div class="cover"><div class="cover-photo" role="img" aria-label="Framed embroidered sampler with alphabets, flower urns, borders and a fruit tree"></div></div>
  <h1 class="cover-title"><span class="line">I am a</span><span class="line">Child of</span><span class="light">LIGHT</span></h1>
  <p class="cover-tagline">I WALK IN LOVE AND LIVE IN BEAUTY</p>
</section>

<section class="spread spread--inside">
  <div class="stitch-rule" style="left:40px;top:22px;width:362px"></div>
  <div class="stitch-rule" style="left:440px;top:22px;width:358px"></div>

  <div class="illustration" role="img" aria-label="Line illustration of an antique sewing machine"></div>

  <div class="essay-col essay-col--left">
    <div class="wrap-gap"></div><div class="wrap-shape"></div>
    <p>Nearly fifty years ago as a young bride in the historic seaport of Newburyport, Massachusetts, I became intrigued by 18th century embroidery samplers, created by young girls as part of their education to learn basic needlework skills needed to operate the family household. Samplers depicting alphabets and numerals served as a pattern book -- from simple cross-stitch, back-stitch and whip-stitch to more elaborate techniques like chain-stitch, blanket-stitch, satin-stitch, and French knots.</p>
    <p>As luck had it, I chanced upon a kit to create a replica of a sampler sewn in 1760 by 11-year-old Newburyporter Edith Hallows. My sewing skills were extremely limited (I am a duct tape &amp; staple hemmer), but I was determined to recreate this charming artifact of colonial life in our picturesque harbor town.</p>
    <p>Four needle-pricking, patience-worn, eye-straining years later, my sampler was nearly finished. Despite my clumsy stitches, it was a silk-threaded marvel of rainbow-colored alphabets, urns of flowers and vines, scrolling flourishes and geometric borders, deer and rabbits gamboling under a fruit tree. Edith’s original sampler – like many -- featured a pious religious statement, so all my piece lacked was a Bible verse or moral quotation that would personalize my piece for posterity. Given the endless pokes, jabs and mind-numbing tedium I had experienced in the making of my sampler, I was tempted to stitch a record of my frustration: “I vow never to attempt a #%$&amp;!# sampler ever again!” Sobered by the potential shame of how this might reflect on me 100 years hence, I instead recalled an inspirational verse I had often used in meditation: “I am a child of light. I walk in love and live in beauty.”</p>
    <p>More aspirational than representative of my life, those words were like a light at the end of a tunnel -- guiding me toward a way of being that I wanted to be more of my default. Words have a power that we don’t often appreciate in</p>
  </div>

  <div class="essay-col essay-col--right">
    <div class="wrap-gap-r"></div><div class="wrap-r1"></div><div class="wrap-r2"></div><div class="wrap-r3"></div>
    <p>ordinary speech, as depicted in many stories about magic spells. There may be a basis of truth at the heart of these fairy tales. For example, the sorcerer’s incantation abracadabra is reputed to come from the Hebrew and means “I create what I speak” – or at root, “what is spoken is what becomes.” With a wave of a wand and recitation of the word, shazam! -- magic can happen!</p>
    <p>This is more than just woo-woo New Age thinking. There’s also science behind how the way we speak and what we say shapes our perceptions, actions and experiences. Positive affirmations can create and strengthen neural pathways in our brain, serving as a kind of unconscious compass to point us in the direction we want to go. For me, the words of my sampler remind me to lean into moments where I feel joy and lightness.</p>
    <p>The dark hours of our being have their place in our lives, and while they can be painful or unwanted, there is even sometimes safety or solace in shadow. In truth, we cannot have one without the other – much like a flower whose petals reach up toward the light must also let its roots dangle deeply in soil. Yet, there are moments like when my beloved grandson Milo reaches up to hug me spontaneously or when a piece of music enthralls me or when the eyes of my barista smile as I put a small tip in her jar, I am indeed “a child of light, walking in love and living in beauty.”</p>
  </div>

  <div class="closing-title"><span class="title">I AM A CHILD OF LIGHT</span><span class="sub">I walk in love and live in beauty</span></div>

  <div class="stitch-rule" style="left:40px;top:511px;width:362px"></div>
  <div class="stitch-rule" style="left:440px;top:511px;width:358px"></div>
</section>

</body>
</html>
```